Brackenfold Latches Business Cards

Need high quality business card designed around my company logo. Ideally the cards need to be a glossy black as the logo goes well with a black background.

The company is a Locksmithing business.

Domestic clients are Residential Home Owners and Landlords. Commercial clients are local businesses, estate agents, landlords, solicitors

Services offered :
Emergency Lock Out
New Lock Fitting & Replacement
High Security Upgrades
UPVC lock repairs
Mobile Key Cutting
Free Security Reviews

Qualificatons & Certifications:
Accredited Guild & Tower KSR Level 3, QTRB
Fully Insured
PVX Checked

Contact & Business Details:

Business Name : Brackenfold Latches
Name: Rob Fenwick
Tel: 01823 574419 Office / 07841592637 Mobile
Email: contact@brackenfoldlatches.com
Website: www.brackenfoldlatches.com

(please note that the website is currently under development and not available to view)

Locksmith

Name: Rob Fenwick

Services:
Emergency Lock Out
High Security Upgrades
UPVC lock repairs
Mobile Key Cutting
Free Security Reviews

• Ideally the cards should be a glossy black as the logo stands out better on a black background.

Logo on front and the word LOCKSMITH should be incorporated into the front design of the card.

Qualifications & Certifications on the back ideally along the top / bottom of the card or split (I.e along the top “ Accredited : Guild & Tower Level 3 , QTRB”
and along the bottom , “Fully Insured & PVX Checked”

Services offered ideally listed on the back of the card, preferably split into two columns. If possible the logo could also be incorporated onto the back of the card between the two services columns (I.e the services listed either side of the logo)
• On the back of the card, have the logo in the middle with the services listed either side of the logo I.e 3 services on left of logo and three to the right.

```html
<!DOCTYPE html>
<html lang="en">
<head>
<meta charset="utf-8">
<title>Brackenfold Latches – Business Cards</title>
<link href="https://fonts.googleapis.com/css2?family=Roboto:wght@400;500&display=swap" rel="stylesheet">
<style>
  :root {
    --page: #141414;
    --card: #0b0b0c;
    --gold: #d8aa2c;
    --gold-deep: #b88c1c;
  }
  * { box-sizing: border-box; margin: 0; padding: 0; }
  html, body {
    width: 1200px; height: 1200px; overflow: hidden;
    background: var(--page);
    font-family: "Roboto", Arial, sans-serif;
    color: var(--gold);
  }
  .sheet {
    width: 1200px; height: 1200px;
    display: flex; flex-direction: column;
    align-items: center; justify-content: center; gap: 40px;
  }
  .card {
    position: relative;
    width: 840px; height: 543px;
    background: var(--card);
    overflow: hidden;
  }

  /* Front */
  .front-brand {
    position: absolute; inset: 0;
    display: flex; align-items: center; justify-content: center; gap: 26px;
  }
  .brand-dot {
    width: 54px; height: 54px; border-radius: 50%;
    background: var(--gold);
    flex: none;
  }
  .front-brand .brand-name {
    font-size: 58px; font-weight: 500; letter-spacing: 1px;
  }

  /* Back */
  .back-left {
    position: absolute; left: 0; top: 0; width: 370px; height: 100%;
  }
  .back-brand {
    position: absolute; top: 74px; left: 0; width: 100%;
    display: flex; align-items: center; justify-content: center; gap: 12px;
  }
  .back-brand .brand-dot { width: 26px; height: 26px; }
  .back-brand .brand-name { font-size: 24px; font-weight: 500; }

  .section-title {
    font-size: 27px; font-weight: 400;
    padding-bottom: 4px;
    border-bottom: 3px solid var(--gold);
    display: inline-block;
  }
  .services {
    position: absolute; right: 22px; top: 170px; text-align: right;
  }
  .services .section-title { margin-bottom: 12px; }
  .service-list { list-style: none; font-size: 18.5px; line-height: 1.42; }

  .divider {
    position: absolute; left: 370px; top: 52px; bottom: 52px;
    width: 2px; background: var(--gold);
  }

  .back-right {
    position: absolute; left: 398px; top: 46px; right: 30px;
  }
  .person-name { font-size: 48px; font-weight: 400; line-height: 1.1; }
  .credentials {
    margin-top: 10px; font-size: 16.5px; line-height: 1.35;
  }
  .contact { margin-top: 30px; }
  .contact .section-title { margin-bottom: 14px; }
  .contact-list { list-style: none; font-size: 17.5px; line-height: 1.6; }
  .social-row {
    display: flex; gap: 14px; margin-top: 16px;
  }
  .social-row span {
    width: 36px; height: 36px;
    border: 2.5px solid var(--gold); border-radius: 8px;
  }
  .base-band {
    position: absolute; left: 0; right: 0; bottom: 0; height: 12px;
    background: var(--gold-deep);
  }
</style>
</head>
<body>
<main class="sheet">
  <section class="card card-front" aria-label="Card front">
    <div class="front-brand">
      <span class="brand-dot"></span>
      <span class="brand-name">Brackenfold Latches</span>
    </div>
  </section>

  <section class="card card-back" aria-label="Card back">
    <div class="back-left">
      <div class="back-brand">
        <span class="brand-dot"></span>
        <span class="brand-name">Brackenfold Latches</span>
      </div>
      <div class="services">
        <h2 class="section-title">Services offered</h2>
        <ul class="service-list">
          <li>Emergency Lock Out</li>
          <li>New Lock Fitting &amp; Replacement</li>
          <li>High Security Upgrades</li>
          <li>UPVC lock repairs</li>
          <li>Mobile Key Cutting</li>
          <li>Free Security Reviews</li>
        </ul>
      </div>
    </div>

    <div class="divider"></div>

    <div class="back-right">
      <h1 class="person-name">Rob Fenwick</h1>
      <p class="credentials">
        Qualificatons &amp; Certifications:<br>
        Accredited Guild &amp; Tower KSR Level 3, QTRB<br>
        Fully Insured<br>
        PVX Checked
      </p>
      <div class="contact">
        <h2 class="section-title">Contact &amp; Business Details</h2>
        <ul class="contact-list">
          <li>contact@brackenfoldlatches.com</li>
          <li>07841592637</li>
          <li>01823 574419</li>
          <li>www.brackenfoldlatches.com</li>
        </ul>
        <div class="social-row" aria-hidden="true">
          <span></span><span></span><span></span><span></span>
        </div>
      </div>
    </div>

    <div class="base-band"></div>
  </section>
</main>
</body>
</html>
```